High end wine label at Austrian Winery

We are a traditional winery in Austria in region Burgenland. We are looking for a relaunch of our current wine label for our [vantor] series. It's a high end wine series at an upper price range. At the moment we have just two kinds of the label, one white one for the white wines and one black one for the red wines. This is a series of wine, white, red, sweet, sparkling and a top wine categories. So we need the same label, but in 4 different ways to distinguish the wines plus the sparkling. Maybe in color, patterns, ... or something else. The label should be very simple, including our new logo. It's also possible to make one label but we can splitting two parts of the label. The size of the label does not matter, need not be the same as now. It's a bit higher than a normal bottle. Additionally we need a back label with wine description and the wine dates on it.

Target Market(s)

private consumers and restaurants, no retailers

Colors

Designer to choose colors to be used in the design.

Requirements
Must have
• simple label with 4 different categories (red, white, sweet, top) plus Frizzante label, new logo integrated, high end label. Just logo, grape variety and [vantor] as text on the front label as text
Nice to have
• It's just good, if there'sa possibility to have different colors of each grape variety (about 10 different), but all the same style. top Wines should have an extraordinary design, but familiar with the others
Should not have
• no cheap look

```html
<!DOCTYPE html>
<html lang="en">
<head>
<meta charset="utf-8">
<title>Halden – [vantor] Wine Label Series</title>
<link href="https://fonts.googleapis.com/css2?family=Jost:wght@300;400;600&display=swap" rel="stylesheet">
<style>
  :root {
    --paper: #ffffff;
    --ink-light: #ffffff;
    --veltliner: #8a7a6b;
    --welschriesling: #b9a56a;
    --pinot-blanc: #93936f;
    --blaufraenkisch: #6a7a82;
    --zweigelt: #a07e6b;
    --merlot: #a07e7c;
    --label-font: "Jost", "Futura", sans-serif;
  }
  * { box-sizing: border-box; margin: 0; padding: 0; }
  html, body {
    width: 1050px;
    height: 1200px;
    overflow: hidden;
    background: var(--paper);
    font-family: var(--label-font);
  }
  .label-series {
    position: relative;
    width: 1050px;
    height: 1200px;
    display: grid;
    grid-template-columns: repeat(3, 305px);
    grid-template-rows: 492px 492px;
    column-gap: 27px;
    row-gap: 120px;
    padding: 50px 0 0 40px;
  }
  .wine-label {
    display: flex;
    flex-direction: column;
    gap: 20px;
  }
  .front-label {
    position: relative;
    height: 464px;
    background: var(--label-color);
    color: var(--ink-light);
  }
  .brand-mark {
    position: absolute;
    top: 42px;
    left: 0;
    right: 0;
    display: flex;
    flex-direction: column;
    align-items: center;
    gap: 12px;
  }
  .brand-mark svg { display: block; }
  .brand-name {
    font-weight: 600;
    font-size: 15px;
    letter-spacing: 2.5px;
    text-transform: uppercase;
  }
  .illustration {
    position: absolute;
    top: 205px;
    left: 62px;
    width: 180px;
    height: 180px;
    border-radius: 6px;
    background: radial-gradient(circle, rgba(255,255,255,0.22) 0%, rgba(255,255,255,0.06) 70%, rgba(255,255,255,0) 100%);
  }
  .grape-variety {
    position: absolute;
    top: 404px;
    left: 0;
    right: 0;
    text-align: center;
    font-weight: 400;
    font-size: 18px;
    letter-spacing: 0.3px;
    text-transform: uppercase;
  }
  .series-strip {
    height: 28px;
    background: var(--label-color);
    color: var(--ink-light);
    display: flex;
    align-items: center;
    justify-content: center;
    font-size: 9.5px;
    font-weight: 400;
    letter-spacing: 1px;
    text-transform: uppercase;
  }
  .veltliner { --label-color: var(--veltliner); }
  .welschriesling { --label-color: var(--welschriesling); }
  .pinot-blanc { --label-color: var(--pinot-blanc); }
  .blaufraenkisch { --label-color: var(--blaufraenkisch); }
  .zweigelt { --label-color: var(--zweigelt); }
  .merlot { --label-color: var(--merlot); }
</style>
</head>
<body>
<main class="label-series">

  <article class="wine-label veltliner">
    <div class="front-label">
      <div class="brand-mark">
        <svg width="60" height="60" viewBox="0 0 60 60" aria-hidden="true"><circle cx="30" cy="30" r="28" fill="none" stroke="#fff" stroke-width="2"/></svg>
        <span class="brand-name">Halden</span>
      </div>
      <div class="illustration" role="img" aria-label="Line drawing of a ship's steering wheel"></div>
      <h2 class="grape-variety">Grüner Veltliner</h2>
    </div>
    <div class="series-strip">[ Vantor ]</div>
  </article>

  <article class="wine-label welschriesling">
    <div class="front-label">
      <div class="brand-mark">
        <svg width="60" height="60" viewBox="0 0 60 60" aria-hidden="true"><circle cx="30" cy="30" r="28" fill="none" stroke="#fff" stroke-width="2"/></svg>
        <span class="brand-name">Halden</span>
      </div>
      <div class="illustration" role="img" aria-label="Line drawing of a scallop shell"></div>
      <h2 class="grape-variety">Welschriesling</h2>
    </div>
    <div class="series-strip">[ Vantor ]</div>
  </article>

  <article class="wine-label pinot-blanc">
    <div class="front-label">
      <div class="brand-mark">
        <svg width="60" height="60" viewBox="0 0 60 60" aria-hidden="true"><circle cx="30" cy="30" r="28" fill="none" stroke="#fff" stroke-width="2"/></svg>
        <span class="brand-name">Halden</span>
      </div>
      <div class="illustration" role="img" aria-label="Line drawing of a tall sailing ship on waves"></div>
      <h2 class="grape-variety">Pinot Blanc</h2>
    </div>
    <div class="series-strip">[ Vantor ]</div>
  </article>

  <article class="wine-label blaufraenkisch">
    <div class="front-label">
      <div class="brand-mark">
        <svg width="60" height="60" viewBox="0 0 60 60" aria-hidden="true"><circle cx="30" cy="30" r="28" fill="none" stroke="#fff" stroke-width="2"/></svg>
        <span class="brand-name">Halden</span>
      </div>
      <div class="illustration" role="img" aria-label="Line drawing of a small fishing boat"></div>
      <h2 class="grape-variety">Blaufränkisch</h2>
    </div>
    <div class="series-strip">[ Vantor ]</div>
  </article>

  <article class="wine-label zweigelt">
    <div class="front-label">
      <div class="brand-mark">
        <svg width="60" height="60" viewBox="0 0 60 60" aria-hidden="true"><circle cx="30" cy="30" r="28" fill="none" stroke="#fff" stroke-width="2"/></svg>
        <span class="brand-name">Halden</span>
      </div>
      <div class="illustration" role="img" aria-label="Line drawing of a lighthouse on rocks"></div>
      <h2 class="grape-variety">Zweigelt</h2>
    </div>
    <div class="series-strip">[ Vantor ]</div>
  </article>

  <article class="wine-label merlot">
    <div class="front-label">
      <div class="brand-mark">
        <svg width="60" height="60" viewBox="0 0 60 60" aria-hidden="true"><circle cx="30" cy="30" r="28" fill="none" stroke="#fff" stroke-width="2"/></svg>
        <span class="brand-name">Halden</span>
      </div>
      <div class="illustration" role="img" aria-label="Line drawing of a branching coral"></div>
      <h2 class="grape-variety">Merlot</h2>
    </div>
    <div class="series-strip">[ Vantor ]</div>
  </article>

</main>
</body>
</html>
```